Vorrel Letterhead

Need a fresh looking design. We are a IT service company and I would like some elements of the logo to flow through. I have included the logo as an attachment. I have also included business card design as it might help with the design.

Industry/Entity Type

Business

```html
<!DOCTYPE html>
<html lang="en">
<head>
<meta charset="utf-8">
<title>Vorrel Letterhead</title>
<link rel="stylesheet" href="https://fonts.googleapis.com/css2?family=Questrial&display=swap">
<style>
  :root {
    --brand-green: #a6ce4a;
    --brand-grey: #818b91;
    --footer-grey: #89939a;
    --shadow-grey: #7a8389;
    --paper: #ffffff;
    --ink-light: #ffffff;
  }
  * { margin: 0; padding: 0; box-sizing: border-box; }
  html, body {
    width: 927px;
    height: 1200px;
    overflow: hidden;
    background: var(--paper);
  }
  .page {
    position: relative;
    width: 927px;
    height: 1200px;
    overflow: hidden;
    background: var(--paper);
  }
  .sheet {
    position: absolute;
    top: 0;
    left: 0;
    width: 1000px;
    height: 1294px;
    transform: scale(0.927);
    transform-origin: 0 0;
    font-family: "Questrial", "Century Gothic", sans-serif;
  }
  .header-art {
    position: absolute;
    top: 0;
    left: 0;
    width: 1000px;
    height: 200px;
  }
  .brand-name {
    position: absolute;
    left: 10px;
    top: 38px;
    width: 310px;
    text-align: center;
    font-size: 80px;
    line-height: 1;
    color: var(--brand-green);
    letter-spacing: 1px;
  }
  .contact-person {
    position: absolute;
    left: 584px;
    top: 40px;
    color: var(--ink-light);
  }
  .person-name {
    font-size: 13px;
    letter-spacing: 0.3px;
  }
  .person-role {
    font-size: 9px;
    color: var(--brand-green);
    margin-top: 1px;
  }
  .contact-list {
    list-style: none;
    font-size: 11px;
    color: var(--ink-light);
  }
  .contact-list li {
    display: flex;
    align-items: center;
    height: 16px;
  }
  .contact-icon {
    width: 12px;
    height: 12px;
    margin-right: 8px;
    flex: none;
  }
  .person-contacts {
    position: absolute;
    left: 584px;
    top: 69px;
  }
  .office-contacts {
    position: absolute;
    left: 756px;
    top: 53px;
  }
  .divider {
    position: absolute;
    left: 739px;
    top: 55px;
    width: 1px;
    height: 62px;
    background: var(--ink-light);
  }
  .footer-band {
    position: absolute;
    left: 0;
    top: 1237px;
    width: 1000px;
    height: 57px;
    background: var(--footer-grey);
  }
</style>
</head>
<body>
<div class="page">
  <div class="sheet">
    <svg class="header-art" viewBox="0 0 1000 200" aria-hidden="true">
      <rect x="0" y="0" width="1000" height="144" fill="var(--brand-green)"/>
      <path d="M300 80 C 480 35, 720 22, 1000 22 L 1000 135 L 300 135 Z" fill="var(--brand-grey)"/>
      <ellipse cx="166" cy="104" rx="160" ry="88" fill="var(--shadow-grey)"/>
      <ellipse cx="162" cy="92" rx="162" ry="92" fill="var(--brand-green)"/>
      <ellipse cx="162" cy="84" rx="158" ry="81" fill="var(--paper)"/>
    </svg>

    <div class="brand-name">Vorrel</div>

    <div class="contact-person">
      <div class="person-name">RJ CALDER</div>
      <div class="person-role">I.T. Consultant</div>
    </div>

    <ul class="contact-list person-contacts">
      <li>
        <svg class="contact-icon" viewBox="0 0 12 12"><circle cx="6" cy="6" r="5.3" fill="none" stroke="var(--brand-green)" stroke-width="1"/><rect x="4.2" y="3" width="3.6" height="6" rx="0.6" fill="none" stroke="var(--brand-green)" stroke-width="0.8"/></svg>
        0400 318 742
      </li>
      <li>
        <svg class="contact-icon" viewBox="0 0 12 12"><circle cx="6" cy="6" r="5.3" fill="none" stroke="var(--brand-green)" stroke-width="1"/><rect x="3.2" y="4" width="5.6" height="4" fill="none" stroke="var(--brand-green)" stroke-width="0.8"/><path d="M3.2 4 L6 6.2 L8.8 4" fill="none" stroke="var(--brand-green)" stroke-width="0.8"/></svg>
        rj@vorrel.com.au
      </li>
    </ul>

    <div class="divider"></div>

    <ul class="contact-list office-contacts">
      <li>
        <svg class="contact-icon" viewBox="0 0 12 12"><circle cx="6" cy="6" r="5.3" fill="none" stroke="var(--brand-green)" stroke-width="1"/><path d="M6 9.2 C 4 7, 3.8 6, 3.8 5.2 A 2.2 2.2 0 0 1 8.2 5.2 C 8.2 6, 8 7, 6 9.2 Z" fill="none" stroke="var(--brand-green)" stroke-width="0.8"/></svg>
        PO Box 2183, Harlow Bay 2041
      </li>
      <li>
        <svg class="contact-icon" viewBox="0 0 12 12"><circle cx="6" cy="6" r="5.3" fill="none" stroke="var(--brand-green)" stroke-width="1"/><path d="M4 3.2 L5.2 3.2 L5.6 4.8 L4.9 5.4 C 5.3 6.3, 5.8 6.8, 6.6 7.2 L7.2 6.5 L8.8 6.9 L8.8 8.1 C 6 8.3, 3.8 6.1, 4 3.2 Z" fill="none" stroke="var(--brand-green)" stroke-width="0.7"/></svg>
        02 9000 4182
      </li>
      <li>
        <svg class="contact-icon" viewBox="0 0 12 12"><circle cx="6" cy="6" r="5.3" fill="none" stroke="var(--brand-green)" stroke-width="1"/><rect x="3.2" y="4.5" width="5.6" height="3.8" fill="none" stroke="var(--brand-green)" stroke-width="0.8"/><rect x="4.2" y="3" width="3.6" height="1.5" fill="none" stroke="var(--brand-green)" stroke-width="0.7"/></svg>
        02 9000 4183
      </li>
      <li>
        <svg class="contact-icon" viewBox="0 0 12 12"><circle cx="6" cy="6" r="5.5" fill="var(--brand-green)"/><circle cx="6" cy="6" r="3" fill="none" stroke="var(--brand-grey)" stroke-width="0.7"/><path d="M3 6 H9 M6 3 C 4.6 4.6, 4.6 7.4, 6 9 M6 3 C 7.4 4.6, 7.4 7.4, 6 9" fill="none" stroke="var(--brand-grey)" stroke-width="0.6"/></svg>
        www.vorrel.com.au
      </li>
    </ul>

    <div class="footer-band"></div>
  </div>
</div>
</body>
</html>
```